VORELT Diagnostics Pooling One Sheet

The process and concept for pooling is to target large populations of people; i.e. a school, prison, employer (where people are isolated by pods), then to test them all in one controllable group. By breaking down the pool size (ideally is 12 or 16 max) then when a positive pool pops up, the entity has the lab automatically reflex to test the whole pool to determine who is positive. During that exchange, several workflows could take place from the population that was being tested. This type of pooled testing is called Surveillance testing ,when it reflects, then it goes to Screening or Diagnostic testing.

The workflow is:
School/employer collects all patient information captured on a requisition form or electronically (w signature) and DOES NOT send to VORELT
School/employer collects individual specimens and labels them with a unique bar code (non-repeating and can include the DOB)
School/employer is responsible for housing and managing all the unique patient information for each individual specimen
School/employer delivers specimens to VORELT and School/employer directs VORELT what specimens are in what designated pool (one pool size for entire project)
When a pool is positive, VORELT notifies School/employer
When reflex testing in indicated for client, School/employer submits to VORELT on demand all patient information needed to process the reflexed option
VORELT reports back to School/employer in 12 hours the results of the retest
https://www.plaxomer.example/medical-devices/coronavirus-covid-19-and-medical-devices/pooled-sample-testing-and-screening-testing-covid-19
https://www.trunvessa.example/coronavirus-disease-covid-19/news/trunvessa-receives-authorization-covid-19-sample-pooling

Target Market(s)

Schools, Universities, Employers

Font styles to use
Sans Serif

Colors
85acd3
85cae6
34a6d7

Requirements
Must have
• VORELT branded along with an elegant yet clinical feel. have all contact information for VORELT Diagnostics. Go to www.vorelthq.example for all info

```html
<!DOCTYPE html>
<html lang="en">
<head>
<meta charset="utf-8">
<title>VORELT Diagnostics – Pooling One Sheet</title>
<link href="https://fonts.googleapis.com/css2?family=Lato:wght@400;700;900&display=swap" rel="stylesheet">
<style>
  :root {
    --backdrop: #e8e5e1;
    --paper: #ffffff;
    --ink: #26323f;
    --navy: #2f3e50;
    --footer-navy: #223554;
    --band-blue: #2f8fd2;
    --band-blue-deep: #1f78c0;
    --accent: #34a6d7;
    --sky: #85cae6;
    --steel: #85acd3;
  }
  * { box-sizing: border-box; margin: 0; padding: 0; }
  html, body {
    width: 1200px; height: 960px; overflow: hidden;
    background: var(--backdrop);
    font-family: "Lato", Arial, sans-serif;
  }
  .sheet-frame { position: relative; width: 1200px; height: 960px; }
  .sheet {
    position: absolute; left: 266px; top: 11px;
    width: 880px; height: 1235px;
    transform: scale(0.76); transform-origin: top left;
    background: var(--paper); overflow: hidden;
    box-shadow: 0 6px 24px rgba(0,0,0,.18);
  }
  .brand {
    position: absolute; left: 70px; top: 68px;
    display: flex; align-items: center; gap: 16px;
  }
  .brand-mark { width: 34px; height: 34px; background: var(--navy); }
  .brand-name { font-weight: 900; font-size: 40px; color: var(--navy); letter-spacing: .5px; }

  .intro-band {
    position: absolute; left: 0; top: 165px; width: 880px; height: 352px;
    background: linear-gradient(135deg, var(--band-blue) 0%, var(--band-blue-deep) 100%);
  }
  .intro-text {
    position: absolute; left: 65px; top: 192px; width: 345px;
    color: #fff; font-size: 16.6px; line-height: 20.8px;
  }
  .hero-photo { position: absolute; left: 0; top: 0; width: 880px; height: 1235px; pointer-events: none; }

  .workflow-title {
    position: absolute; left: 65px; top: 555px; height: 48px;
    padding: 0 28px 0 20px; background: var(--navy); color: #fff;
    border-radius: 0 24px 24px 0;
    font-weight: 900; font-size: 25px; line-height: 48px; letter-spacing: -.3px;
  }
  .workflow-list {
    position: absolute; left: 65px; top: 624px; width: 730px; list-style: none;
  }
  .workflow-list li {
    position: relative; padding-left: 34px; margin-bottom: 9px;
    font-size: 16.6px; line-height: 21px; color: var(--ink);
  }
  .workflow-list .tick { position: absolute; left: 0; top: 2px; width: 20px; height: 20px; }

  .reference-band {
    position: absolute; left: 0; top: 972px; width: 880px; height: 166px;
    background: linear-gradient(120deg, var(--band-blue) 0%, var(--accent) 60%, var(--band-blue) 100%);
  }
  .reference-rule { position: absolute; left: 71px; top: 1000px; width: 3px; height: 105px; background: rgba(255,255,255,.75); }
  .reference-links {
    position: absolute; left: 99px; top: 1030px; width: 740px;
    color: #fff; font-weight: 700; font-size: 17px; line-height: 22px;
    overflow-wrap: anywhere;
  }
  .reference-links p + p { margin-top: 12px; }

  .contact-bar {
    position: absolute; left: 0; top: 1137px; width: 880px; height: 98px;
    background: linear-gradient(90deg, var(--footer-navy), #2a4470 60%, var(--footer-navy));
    display: flex; align-items: center; justify-content: space-between;
    padding: 0 52px 0 66px; color: #fff; font-size: 14.5px; line-height: 17px;
  }
  .contact-item { display: flex; align-items: center; gap: 12px; }
  .contact-item svg { width: 18px; height: 18px; flex: none; }
</style>
</head>
<body>
<div class="sheet-frame">
  <article class="sheet">
    <header class="brand">
      <span class="brand-mark"></span>
      <span class="brand-name">VORELT Diagnostics</span>
    </header>

    <section class="intro-band"></section>
    <p class="intro-text">The process and concept for pooling is to target large populations of people; i.e. a school, prison, employer (where people are isolated by pods), then to test them all in one controllable group. By breaking down the pool size (ideally is 12 or 16 max) then when a positive pool pops up, the entity has the lab automatically reflex to test the whole pool to determine who is positive. During that exchange, several workflows could take place from the population that was being tested. This type of pooled testing is called Surveillance testing, when it reflects, then it goes to Screening or Diagnostic testing.</p>

    <svg class="hero-photo" viewBox="0 0 880 1235" role="img" aria-label="Photo: clinician in white protective suit and face shield taking a throat swab from a patient">
      <defs>
        <linearGradient id="heroTone" x1="0" y1="0" x2="1" y2="1">
          <stop offset="0" stop-color="#eef2f6"/>
          <stop offset=".55" stop-color="#d7e2ec"/>
          <stop offset="1" stop-color="#9fbde0"/>
        </linearGradient>
      </defs>
      <polygon points="682,49 917,169 917,454 682,570 447,454 447,169" fill="url(#heroTone)" stroke="#ffffff" stroke-width="14" stroke-linejoin="round"/>
    </svg>

    <h2 class="workflow-title">THE WORKFLOW IS</h2>
    <ul class="workflow-list">
      <li><svg class="tick" viewBox="0 0 20 20"><circle cx="10" cy="10" r="8.5" fill="none" stroke="#34a6d7" stroke-width="1.8"/><path d="M6 10.2l2.7 2.6L14 7.6" fill="none" stroke="#34a6d7" stroke-width="1.8"/></svg>School/employer collects all patient information captured on a requisition form or electronically (w signature) and DOES NOT send to VORELT</li>
      <li><svg class="tick" viewBox="0 0 20 20"><circle cx="10" cy="10" r="8.5" fill="none" stroke="#34a6d7" stroke-width="1.8"/><path d="M6 10.2l2.7 2.6L14 7.6" fill="none" stroke="#34a6d7" stroke-width="1.8"/></svg>School/employer collects individual specimens and labels them with a unique bar code (non-repeating and can include the DOB)</li>
      <li><svg class="tick" viewBox="0 0 20 20"><circle cx="10" cy="10" r="8.5" fill="none" stroke="#34a6d7" stroke-width="1.8"/><path d="M6 10.2l2.7 2.6L14 7.6" fill="none" stroke="#34a6d7" stroke-width="1.8"/></svg>School/employer is responsible for housing and managing all the unique patient information for each individual specimen</li>
      <li><svg class="tick" viewBox="0 0 20 20"><circle cx="10" cy="10" r="8.5" fill="none" stroke="#34a6d7" stroke-width="1.8"/><path d="M6 10.2l2.7 2.6L14 7.6" fill="none" stroke="#34a6d7" stroke-width="1.8"/></svg>School/employer delivers specimens to VORELT and School/employer directs VORELT what specimens are in what designated pool (one pool size for entire project)</li>
      <li><svg class="tick" viewBox="0 0 20 20"><circle cx="10" cy="10" r="8.5" fill="none" stroke="#34a6d7" stroke-width="1.8"/><path d="M6 10.2l2.7 2.6L14 7.6" fill="none" stroke="#34a6d7" stroke-width="1.8"/></svg>When a pool is positive, VORELT notifies School/employer</li>
      <li><svg class="tick" viewBox="0 0 20 20"><circle cx="10" cy="10" r="8.5" fill="none" stroke="#34a6d7" stroke-width="1.8"/><path d="M6 10.2l2.7 2.6L14 7.6" fill="none" stroke="#34a6d7" stroke-width="1.8"/></svg>When reflex testing in indicated for client, School/employer submits to VORELT on demand all patient information needed to process the reflexed option</li>
      <li><svg class="tick" viewBox="0 0 20 20"><circle cx="10" cy="10" r="8.5" fill="none" stroke="#34a6d7" stroke-width="1.8"/><path d="M6 10.2l2.7 2.6L14 7.6" fill="none" stroke="#34a6d7" stroke-width="1.8"/></svg>VORELT reports back to School/employer in 12 hours the results of the retest</li>
    </ul>

    <section class="reference-band"></section>
    <span class="reference-rule"></span>
    <div class="reference-links">
      <p>https://www.plaxomer.example/medical-devices/coronavirus-covid-19-and-medical-devices/pooled-sample-testing-and-screening-testing-covid-19</p>
      <p>https://www.trunvessa.example/coronavirus-disease-covid-19/news/trunvessa-receives-authorization-covid-19-sample-pooling</p>
    </div>

    <footer class="contact-bar">
      <div class="contact-item">
        <svg viewBox="0 0 20 20"><path d="M5 2.5l3 3.2-1.6 2.2c.9 1.9 2.2 3.3 4.1 4.3l2.1-1.6 3.3 2.9-1.7 2.9C9 16 3.6 10.6 2.5 4.3z" fill="none" stroke="#fff" stroke-width="1.6" stroke-linejoin="round"/></svg>
        <span>855-310-VRLT (8758)</span>
      </div>
      <div class="contact-item">
        <svg viewBox="0 0 20 20"><path d="M10 18s-5.5-5.6-5.5-9.8a5.5 5.5 0 0111 0C15.5 12.4 10 18 10 18z" fill="#fff"/><circle cx="10" cy="8.2" r="2" fill="#223554"/></svg>
        <span>4120 Meridian Park Drive Suite B<br>Aldenford, MD 21790</span>
      </div>
      <div class="contact-item">
        <svg viewBox="0 0 20 20"><rect x="2" y="4.5" width="16" height="11" rx="1" fill="none" stroke="#fff" stroke-width="1.6"/><path d="M2.5 5l7.5 6 7.5-6" fill="none" stroke="#fff" stroke-width="1.6"/></svg>
        <span>info@vorelthq.example</span>
      </div>
      <div class="contact-item">
        <svg viewBox="0 0 20 20"><circle cx="10" cy="10" r="7.5" fill="none" stroke="#fff" stroke-width="1.6"/><ellipse cx="10" cy="10" rx="3.2" ry="7.5" fill="none" stroke="#fff" stroke-width="1.3"/><path d="M2.5 10h15" stroke="#fff" stroke-width="1.3"/></svg>
        <span>www.vorelthq.example</span>
      </div>
    </footer>
  </article>
</div>
</body>
</html>
```